House Cleaning company in need of handout re-designs

We are looking to create a 2 sided, full color, 6" x 4" handout that promotes the company www.dustly.com

We have one in existence that performed well, but find it too busy and would like another one designed to test performance (please see the attached files for original design). We are looking for one additional design, however depending on quality of work submitted we will select up to 5 designs.

We are looking for clean designs the will improve performance and you are 'carte blanche' on the design. That said, please ensure the following elements are present:

1) Space for an offer (i.e $39 for 3 hours of cleaning) with an expiry date.
2) Unique URL
3) Promo Code
4) Phone Number
5) The tagline of "Let Dustly handle it" is present.
6) Logo
7) Brand colors are maintained

Also, please highlight the following:

*Eco-Friendly Cleaning Services
*Fully-Screened Cleaning Experts
*60-point checklist
*Easy Online Booking Process

Thank you.

House Cleaning

```html
<!DOCTYPE html>
<html lang="en">
<head>
<meta charset="utf-8">
<title>Dustly.com – Handout, Front and Back</title>
<link rel="stylesheet" href="https://fonts.googleapis.com/css2?family=Anton&family=Courier+Prime:wght@400;700&family=Playfair+Display:ital,wght@0,700;1,700&family=Special+Elite&display=swap">
<style>
  :root {
    --mint: #7fe8b2;
    --mint-deep: #5fd79a;
    --pink: #ec5b7b;
    --pink-deep: #d94d6b;
    --blush: #f7d6e2;
    --white: #ffffff;
    --ink: #2a2a2a;
    --page: #ffffff;
  }
  * { box-sizing: border-box; margin: 0; padding: 0; }
  html, body {
    width: 1200px; height: 900px; overflow: hidden;
    background: var(--page);
  }
  .canvas { position: relative; width: 1200px; height: 900px; }

  .card {
    position: absolute; width: 600px; height: 400px; overflow: hidden;
    box-shadow: 4px 6px 10px rgba(0,0,0,.35);
  }

  /* ---------- Front ---------- */
  .card--front { left: 40px; top: 40px; background: var(--mint); }
  .front-band { position: absolute; inset: 0; }
  .brand {
    font-family: "Playfair Display", Georgia, serif;
    font-weight: 700; color: var(--pink); white-space: nowrap;
  }
  .front-brand {
    position: absolute; left: 50px; top: 120px; font-size: 58px;
    transform: rotate(-18deg); transform-origin: left center;
  }
  .front-figure {
    position: absolute; left: 330px; top: 72px; width: 260px; height: 260px;
    border-radius: 50%; background: var(--white);
  }
  .front-figure .figure-art {
    position: absolute; inset: 30px 50px 20px 50px; border-radius: 40% 40% 30% 30%;
    background: radial-gradient(circle at 50% 60%, var(--blush), #f3c9a0 55%, #c6e87a 80%);
  }

  .offer {
    position: absolute; border-radius: 50%; background: var(--mint-deep);
    display: flex; align-items: center; justify-content: center;
  }
  .offer-disc {
    border-radius: 50%; background: var(--pink-deep);
    border: 3px solid var(--white); outline: 4px solid var(--mint);
    display: flex; flex-direction: column; align-items: center; justify-content: center;
    color: var(--white); text-align: center;
  }
  .offer-hours {
    font-family: "Courier Prime", monospace; font-weight: 700;
    font-size: 18px; line-height: 1.1; letter-spacing: 1px;
  }
  .offer-price {
    font-family: "Anton", Impact, sans-serif; font-size: 52px; line-height: 1;
    color: var(--white); text-shadow: 2px 2px 0 var(--mint-deep);
  }
  .offer-note { font-family: "Courier Prime", monospace; font-size: 12px; letter-spacing: 1px; }
  .offer-code {
    font-family: "Courier Prime", monospace; font-size: 10px; margin-top: 3px;
    border-top: 1px solid var(--white); padding-top: 2px;
  }
  .offer-code b { display: block; font-size: 11px; }

  .card--front .offer { left: 20px; top: 190px; width: 210px; height: 210px; }
  .card--front .offer-disc { width: 170px; height: 170px; }

  /* ---------- Back ---------- */
  .card--back { left: 560px; top: 460px; background: var(--white); }
  .tagline {
    position: absolute; left: 48px; top: 22px; width: 390px;
    font-family: "Special Elite", "Courier New", monospace;
    font-size: 34px; font-weight: 400; line-height: 1.15; color: var(--pink); opacity: .85;
  }
  .tagline span { display: block; padding-left: 70px; }
  .rule { position: absolute; height: 0; border-top: 3px dotted #555; }
  .contact {
    position: absolute; left: 110px;
    font-family: "Courier Prime", monospace; font-weight: 700;
    color: var(--mint-deep); font-size: 22px; letter-spacing: 1px; white-space: nowrap;
  }
  .contact--phone { top: 120px; }
  .contact--url { top: 152px; left: 80px; }

  .back-figure {
    position: absolute; left: 430px; top: 60px; width: 150px; height: 175px;
    border-radius: 45% 45% 20% 20%;
    background: radial-gradient(circle at 50% 45%, #f3c9a0, var(--blush) 55%, #c6e87a 85%);
  }
  .back-band {
    position: absolute; left: 0; bottom: 0; width: 100%; height: 110px;
    background: var(--mint);
  }
  .back-logo {
    position: absolute; left: 385px; top: 235px; width: 210px; height: 56px;
    border: 2px dashed var(--pink); background: var(--white);
    display: flex; align-items: center; justify-content: center;
    font-size: 34px;
  }
  .features {
    position: absolute; left: 222px; top: 304px; list-style: none;
    display: grid; grid-template-columns: 202px 166px; column-gap: 6px; row-gap: 5px;
    font-family: "Playfair Display", Georgia, serif; font-weight: 700;
    font-size: 11.5px; line-height: 16px; color: var(--white); white-space: nowrap;
  }
  .features li::before {
    content: ""; display: inline-block; width: 6px; height: 6px; margin-right: 5px;
    border: 1.5px solid var(--white); border-radius: 50%; vertical-align: middle;
  }
  .card--back .offer { left: 20px; top: 198px; width: 190px; height: 190px; background: var(--mint); }
  .card--back .offer-disc { width: 152px; height: 152px; outline: none; border: none; }
  .card--back .offer-price { text-shadow: none; }
  .expiry { font-family: "Courier Prime", monospace; font-size: 9px; letter-spacing: 1px; }
  .back-code {
    position: absolute; left: 26px; bottom: 8px;
    font-family: "Courier Prime", monospace; font-size: 11px; color: var(--ink);
  }
  .back-code b { letter-spacing: .5px; }
</style>
</head>
<body>
<main class="canvas">

  <section class="card card--front" aria-label="Handout front">
    <svg class="front-band" viewBox="0 0 600 400" aria-hidden="true">
      <polygon points="0,150 430,0 600,0 600,60 0,300" fill="#ffffff"/>
      <line x1="0" y1="150" x2="430" y2="0" stroke="#ec5b7b" stroke-width="5" stroke-dasharray="3 2"/>
      <line x1="0" y1="300" x2="600" y2="60" stroke="#ec5b7b" stroke-width="5" stroke-dasharray="3 2"/>
    </svg>
    <div class="brand front-brand">Dustly.com</div>
    <div class="front-figure">
      <div class="figure-art" role="img" aria-label="Cartoon cleaning lady holding a spray bottle"></div>
    </div>
    <div class="offer">
      <div class="offer-disc">
        <p class="offer-hours">3 HOURS<br>OF CLEANING</p>
        <p class="offer-price">$39</p>
        <p class="offer-note">A $105 Value!</p>
        <p class="offer-code"><b>Promocode</b>9QUAECUSAM</p>
      </div>
    </div>
  </section>

  <section class="card card--back" aria-label="Handout back">
    <h1 class="tagline">Let Dustly handle<span>it!</span></h1>
    <div class="rule" style="left:60px;top:112px;width:330px"></div>
    <p class="contact contact--phone">1-800-8DUSTLY</p>
    <div class="rule" style="left:40px;top:164px;width:34px"></div>
    <p class="contact contact--url">WWW.DUSTLY.COM/CA39</p>
    <div class="back-figure" role="img" aria-label="Cartoon cleaning lady holding a spray bottle"></div>
    <div class="back-band"></div>
    <div class="brand back-logo">Dustly.com</div>
    <ul class="features">
      <li>Eco-Friendly Cleaning Services</li>
      <li>Satisfaction Assured</li>
      <li>Fully-Screened Cleaning Experts</li>
      <li>Easy Online Booking Process</li>
      <li>60-Point Checklist</li>
    </ul>
    <div class="offer">
      <div class="offer-disc">
        <p class="offer-hours">3 HOURS<br>OF CLEANING</p>
        <p class="offer-price">$39</p>
        <p class="expiry">EXPIRES 12/31/15</p>
      </div>
    </div>
    <p class="back-code"><b>Promocode</b> 9QUAECUSAM</p>
  </section>

</main>
</body>
</html>
```